Infoblatt
Zielgruppe
Talentförderung, Personalentwicklung, Beratung von Personalabteilungen
Zielgruppe: Personaler, HR Verantwortliche
Aufgabenstellung
Es geht um einen "One-Pager", der auf einem Kongress ausgelegt werden soll und in Kurzform einen Überblick über unser Unternehmen und unser Angebot informieren soll.
Wir haben Visitenkarten auf Recyclingpapier und möchten das Blatt konsistent auf das gleiche Papier drucken lassen, daher einfarbig schwarz. Format DIN A4 Hoch.
IDEE: Vom Stil wie eine Infografik aufbauen
TYPO: unser LOGO ist BEBAS NEUE und unsere Schrift Helvetica

```html
<!DOCTYPE html>
<html lang="de">
<head>
<meta charset="utf-8">
<title>Lumara – Infoblatt</title>
<link rel="stylesheet" href="https://fonts.googleapis.com/css2?family=Arimo:wght@400;700&display=swap">
<style>
  :root {
    --stage: #2b2b2b;
    --paper: #ffffff;
    --ink: #1a1a1a;
    --ink-soft: #3a3a3a;
    --photo-light: #e6e6e6;
    --photo-mid: #bdbdbd;
    --photo-dark: #8e8e8e;
    --rule: #9a9a9a;
  }
  * { box-sizing: border-box; margin: 0; padding: 0; }
  html, body {
    width: 1200px; height: 804px; overflow: hidden;
    background: var(--stage);
    font-family: "Arimo", "Helvetica Neue", Helvetica, Arial, sans-serif;
    color: var(--ink);
  }
  .sheet {
    position: absolute; left: 331px; top: 22px;
    width: 538px; height: 760px;
    background: var(--paper);
    overflow: hidden;
  }
  .backdrop {
    position: absolute; left: 0; top: 0; width: 538px; height: 424px;
    background:
      radial-gradient(ellipse at 40% 30%, rgba(255,255,255,.55), rgba(255,255,255,0) 60%),
      linear-gradient(90deg, var(--photo-mid) 0%, var(--photo-light) 35%, var(--photo-mid) 60%, var(--photo-light) 85%, var(--photo-mid) 100%);
  }
  .topnav {
    position: absolute; left: 0; top: 18px; width: 538px; height: 42px;
    display: flex; align-items: flex-start; justify-content: space-around;
    padding: 8px 20px 0 40px;
    border-bottom: 1px solid var(--rule);
    background: rgba(255,255,255,.45);
  }
  .topnav span { font-size: 13px; line-height: 1.15; text-align: center; color: var(--ink); }
  .portrait {
    position: absolute; border-radius: 50%;
    background: radial-gradient(circle at 50% 40%, var(--photo-dark), var(--photo-mid) 55%, rgba(230,230,230,0) 72%);
  }
  .portrait--lead { left: 54px; top: 64px; width: 130px; height: 122px; }
  .portrait--hr { left: 362px; top: 150px; width: 94px; height: 108px; }
  .portrait--org { left: 72px; top: 290px; width: 82px; height: 106px; }
  .benefit { position: absolute; font-size: 12px; line-height: 1.3; color: var(--ink-soft); }
  .benefit h2 { font-size: 12px; font-weight: 700; color: var(--ink); }
  .benefit--lead { left: 112px; top: 184px; width: 230px; }
  .benefit--hr { left: 269px; top: 268px; width: 250px; }
  .benefit--org { left: 161px; top: 328px; width: 200px; }
  .brand {
    position: absolute; left: 14px; top: 432px;
    font-size: 38px; font-weight: 700; line-height: 1; color: var(--ink);
  }
  .roll-photo {
    position: absolute; left: 0; top: 478px; width: 246px; height: 282px;
    background: linear-gradient(160deg, var(--photo-light) 0%, #f4f4f4 45%, var(--photo-mid) 100%);
  }
  .about {
    position: absolute; left: 258px; top: 432px; width: 264px;
    font-size: 11.5px; line-height: 1.32; color: var(--ink);
  }
  .about p + p { margin-top: 11px; }
</style>
</head>
<body>
  <main class="sheet">
    <div class="backdrop" role="img" aria-label="Unscharfes Schwarzweißfoto mit Holzstruktur als Hintergrund"></div>

    <nav class="topnav">
      <span>Talentförderung</span>
      <span>Personalentwicklung</span>
      <span>Beratung für<br>Personalabteilungen</span>
    </nav>

    <div class="portrait portrait--lead" role="img" aria-label="Porträtfoto einer Beraterin"></div>
    <section class="benefit benefit--lead">
      <h2>Mehrwert für Führungskräfte</h2>
      <p>Wer führt und wie nicht? Wir entwickeln Führungskompetenz in Ihrer Organisation.</p>
    </section>

    <div class="portrait portrait--hr" role="img" aria-label="Porträtfoto eines Beraters"></div>
    <section class="benefit benefit--hr">
      <h2>Der Personalbereich als Wertschöpfer</h2>
      <p>Was macht HR-Projekte erfolgreich? Wir beraten Sie in Ihrer Personalarbeit.</p>
    </section>

    <div class="portrait portrait--org" role="img" aria-label="Porträtfoto eines Beraters"></div>
    <section class="benefit benefit--org">
      <h2>Mehrwert für Organisationen</h2>
      <p>Wie gelingen Veränderungsprozesse? Wir begleiten Sie dabei.</p>
    </section>

    <div class="brand">LUMARA</div>
    <div class="roll-photo" role="img" aria-label="Schwarzweißfoto gerollter Papierbögen"></div>

    <section class="about">
      <p>Gemeinsam haben wir über 20 Jahre Praxiserfahrung im Personalwesen.</p>
      <p>Wir wissen, inwieweit ein externer Berater Unternehmen unterstützen kann und sollte, gleichzeitig kennen wir die Grenzen dieser Verbindung.</p>
      <p>Die Tücken liegen in der Umsetzung – nämlich dann, wenn der Berater nicht mehr im Haus ist.</p>
      <p>Daher legen wir besonderes Augenmerk auf partnerschaftliche Zusammenarbeit mit unseren Mandanten im Sinne der Nachhaltigkeit unserer Tätigkeit.</p>
    </section>
  </main>
</body>
</html>
```